Update Business Card Design

I'm looking to update my business cards. Attached is a photo of the current design. I like the black side so that does not have to be update. The white side needs to be updated. I want the design to be modern and minimalistic.
I am a lawyer and my firm's website is www.brennoxlegalco.com (for reference).
My firm's logo has a horizontal version (which is on the black side of the card) and a vertical version (on the white side). I would prefer to keep the vertical version on the white side and horizontal version on the black side (the logo files are attached).

I am open to redesigning the black side also. I would like one side to have the horizontal logo and the other to have the vertical logo.

```html
<!DOCTYPE html>
<html lang="en">
<head>
<meta charset="utf-8">
<title>Brennox Legal Co. — Business Card</title>
<link rel="stylesheet" href="https://fonts.googleapis.com/css2?family=Cinzel:wght@400;500&family=Lora:wght@400;700&display=swap">
<style>
  :root {
    --page: #e9e6e1;
    --card-dark: #1c1c1c;
    --card-light: #ffffff;
    --accent: #00b2dd;
    --text-light: #f2f2f2;
    --rule-grey: #5a5a5a;
  }
  * { box-sizing: border-box; margin: 0; padding: 0; }
  html, body { width: 1189px; height: 1200px; overflow: hidden; }
  body { background: var(--page); position: relative; }

  .card {
    position: absolute;
    left: 169px;
    width: 851px;
    height: 484px;
    border-radius: 36px;
    overflow: hidden;
    box-shadow: 0 6px 18px rgba(0,0,0,.18);
  }
  .card--front { top: 112px; background: var(--card-dark); }
  .card--back { top: 641px; background: var(--card-dark); }

  /* Front: horizontal lockup */
  .lockup-horizontal {
    position: absolute;
    left: 0; right: 0; top: 168px;
    display: flex; align-items: center; justify-content: center; gap: 28px;
  }
  .lockup-horizontal .mark-dot {
    width: 92px; height: 92px; border-radius: 50%; background: var(--accent);
  }
  .lockup-horizontal .divider {
    width: 2px; height: 140px; background: var(--text-light);
  }
  .lockup-horizontal .firm-name {
    font-family: "Cinzel", serif; font-weight: 500;
    color: var(--accent); font-size: 54px; line-height: 1.12;
  }
  .website {
    position: absolute; left: 0; right: 0; top: 364px;
    text-align: center;
    font-family: "Cinzel", serif; font-size: 22px; letter-spacing: 2.5px;
    color: var(--text-light);
  }

  /* Back */
  .back-shape { position: absolute; inset: 0; }
  .name-tab {
    position: absolute; left: -27px; top: 67px;
    width: 54px; height: 54px; border-radius: 50%; background: var(--accent);
  }
  .person-name {
    position: absolute; left: 46px; top: 64px;
    font-family: "Lora", serif; font-weight: 700; font-size: 29px;
    color: var(--text-light); letter-spacing: .3px;
  }
  .person-title {
    position: absolute; left: 46px; top: 98px;
    font-family: "Lora", serif; font-size: 20px; color: var(--accent);
  }
  .address {
    position: absolute; left: 46px; top: 196px;
    font-family: "Lora", serif; font-size: 20px; line-height: 25.5px;
    color: var(--text-light); font-style: normal;
  }
  .contact-list {
    position: absolute; left: 46px; top: 307px; list-style: none;
    font-family: "Lora", serif; font-size: 19.5px; color: var(--text-light);
  }
  .contact-list li {
    display: flex; align-items: center; gap: 14px; height: 27.5px;
  }
  .contact-icon {
    width: 23px; height: 23px; border-radius: 3px; background: var(--accent);
    display: flex; align-items: center; justify-content: center; flex: none;
  }
  .contact-icon svg { width: 15px; height: 15px; }

  .lockup-vertical {
    position: absolute; left: 480px; width: 330px; top: 88px;
    display: flex; flex-direction: column; align-items: center;
  }
  .lockup-vertical .mark-dot {
    width: 120px; height: 120px; border-radius: 50%; background: var(--accent);
  }
  .lockup-vertical .rule {
    width: 218px; height: 3px; border-radius: 2px;
    background: var(--rule-grey); margin: 44px 0 18px;
  }
  .lockup-vertical .firm-name {
    font-family: "Cinzel", serif; font-weight: 500; text-align: center;
    color: var(--accent); font-size: 42px; line-height: 1.15;
  }
</style>
</head>
<body>

<section class="card card--front">
  <div class="lockup-horizontal">
    <span class="mark-dot"></span>
    <span class="divider"></span>
    <p class="firm-name">Brennox<br>Legal Co.</p>
  </div>
  <p class="website">www.brennoxlegalco.com</p>
</section>

<section class="card card--back">
  <svg class="back-shape" width="851" height="484" viewBox="0 0 851 484" aria-hidden="true">
    <rect width="851" height="484" fill="var(--card-dark)"/>
    <path d="M440 0 Q326 242 440 484 L446 484 Q338 242 446 0 Z" fill="var(--accent)"/>
    <path d="M452 0 Q346 242 452 484 H851 V0 Z" fill="var(--card-light)"/>
  </svg>

  <span class="name-tab"></span>
  <h1 class="person-name">DANIEL MORROW</h1>
  <p class="person-title">Attorney at Law</p>

  <address class="address">
    218 Alder Crest Avenue<br>
    Suite 410<br>
    Westbrook, CA 90318
  </address>

  <ul class="contact-list">
    <li>
      <span class="contact-icon"><svg viewBox="0 0 16 16"><rect x="4" y="1.5" width="8" height="13" rx="1.5" fill="none" stroke="#1c1c1c" stroke-width="1.6"/></svg></span>
      555.204.1187
    </li>
    <li>
      <span class="contact-icon"><svg viewBox="0 0 16 16"><path d="M2 6 Q8 1 14 6 L12.5 8 L10.5 7 L10.5 5.5 Q8 4.5 5.5 5.5 L5.5 7 L3.5 8 Z" fill="#1c1c1c"/><rect x="3.5" y="9" width="9" height="5" rx="1" fill="#1c1c1c"/></svg></span>
      555.381.6620
    </li>
    <li>
      <span class="contact-icon"><svg viewBox="0 0 16 16"><rect x="4.5" y="1.5" width="7" height="4" fill="#1c1c1c"/><rect x="2" y="6" width="12" height="6" rx="1" fill="#1c1c1c"/><rect x="4.5" y="10" width="7" height="4.5" fill="#1c1c1c" stroke="#00b2dd" stroke-width="1"/></svg></span>
      555.381.6645
    </li>
    <li>
      <span class="contact-icon"><svg viewBox="0 0 16 16"><rect x="2" y="4" width="12" height="8.5" fill="none" stroke="#1c1c1c" stroke-width="1.4"/><path d="M2 4 L8 9 L14 4" fill="none" stroke="#1c1c1c" stroke-width="1.4"/></svg></span>
      daniel@BrennoxLegalCo.com
    </li>
  </ul>

  <div class="lockup-vertical">
    <span class="mark-dot"></span>
    <span class="rule"></span>
    <p class="firm-name">Brennox<br>Legal Co.</p>
  </div>
</section>

</body>
</html>
```